Business cards for Harbourline Supply Pty Ltd that import building products into Australia from China
Target Market(s)
Business to Business
Industry/Entity Type
Business
Contact Information for Business Card
Front: Logo and Business Name
Rear:
Vernon Ashcombe
General Manager
Mobile: 0427 619 354
email: vern@harbourlinesupply.com.au
alternative email: vern@coastwardgoods.com.au
web: www.harbourlinesupply.com.au
Adelaide, Brisbane and Darwin
Colors
ec1f27
fbee3d

```html
<!DOCTYPE html>
<html lang="en">
<head>
<meta charset="utf-8">
<title>Harbourline Supply Pty Ltd – Business Cards</title>
<link href="https://fonts.googleapis.com/css2?family=Open+Sans:wght@300;400;700&family=Oswald:wght@500&display=swap" rel="stylesheet">
<style>
  :root {
    --backdrop: #1a1a1a;
    --card: #262626;
    --ink: #ffffff;
    --ink-soft: #e4e4e4;
    --accent: #ec1f27;
    --rule: #8a8a8a;
  }
  * { margin: 0; padding: 0; box-sizing: border-box; }
  html, body {
    width: 1200px;
    height: 1000px;
    overflow: hidden;
    background: var(--backdrop);
    font-family: "Open Sans", Arial, sans-serif;
  }
  .sheet {
    position: relative;
    width: 1200px;
    height: 1000px;
  }
  .card {
    position: absolute;
    left: 250px;
    width: 700px;
    height: 400px;
    background: var(--card);
    box-shadow: 0 10px 30px rgba(0,0,0,.45);
    overflow: hidden;
  }
  .card--front { top: 70px; }
  .card--back  { top: 530px; }

  /* Front */
  .brand {
    position: absolute;
    inset: 0;
    display: flex;
    align-items: center;
    justify-content: center;
    gap: 14px;
  }
  .brand__mark {
    width: 16px;
    height: 16px;
    background: var(--accent);
  }
  .brand__name {
    font-weight: 700;
    font-size: 30px;
    letter-spacing: .5px;
    color: var(--ink);
    text-transform: uppercase;
  }

  /* Back */
  .identity {
    position: absolute;
    top: 142px;
    right: 372px;
    text-align: right;
  }
  .identity__name {
    font-family: "Oswald", "Arial Narrow", sans-serif;
    font-weight: 500;
    font-size: 34px;
    line-height: 1;
    color: var(--ink);
    text-transform: uppercase;
    letter-spacing: .5px;
    white-space: nowrap;
  }
  .identity__role {
    font-size: 17px;
    line-height: 1.2;
    color: var(--accent);
    letter-spacing: .5px;
  }
  .divider {
    position: absolute;
    left: 344px;
    top: 130px;
    width: 2px;
    height: 92px;
    background: var(--rule);
  }
  .contacts {
    position: absolute;
    left: 362px;
    top: 128px;
    list-style: none;
  }
  .contacts li {
    display: flex;
    align-items: center;
    gap: 12px;
    height: 24px;
    font-weight: 300;
    font-size: 15px;
    color: var(--ink-soft);
    letter-spacing: .3px;
    white-space: nowrap;
  }
  .contacts strong { font-weight: 400; }
  .icon { width: 13px; height: 13px; fill: var(--accent); flex: none; }
  .address {
    position: absolute;
    left: 70px;
    top: 292px;
    display: flex;
    align-items: center;
    gap: 10px;
    font-weight: 300;
    font-size: 17px;
    color: var(--ink-soft);
    letter-spacing: .6px;
  }
  .address .icon { width: 14px; height: 18px; }
</style>
</head>
<body>
<main class="sheet">
  <section class="card card--front" aria-label="Card front">
    <div class="brand">
      <span class="brand__mark"></span>
      <span class="brand__name">Harbourline Supply Pty Ltd</span>
    </div>
  </section>

  <section class="card card--back" aria-label="Card back">
    <div class="identity">
      <h1 class="identity__name">Vernon Ashcombe</h1>
      <p class="identity__role">General Manager</p>
    </div>
    <span class="divider"></span>
    <ul class="contacts">
      <li>
        <svg class="icon" viewBox="0 0 24 24" aria-hidden="true"><path d="M6.6 10.8a15.1 15.1 0 0 0 6.6 6.6l2.2-2.2a1 1 0 0 1 1-.25 11.4 11.4 0 0 0 3.6.57 1 1 0 0 1 1 1V20a1 1 0 0 1-1 1A17 17 0 0 1 3 4a1 1 0 0 1 1-1h3.5a1 1 0 0 1 1 1c0 1.25.2 2.45.57 3.57a1 1 0 0 1-.25 1z"/></svg>
        0427 619 354
      </li>
      <li>
        <svg class="icon" viewBox="0 0 24 24" aria-hidden="true"><path d="M2 6.5V19h20V6.5l-10 7.5z M3 5h18l-9 6.8z"/></svg>
        vern@harbourlinesupply.com.au
      </li>
      <li>
        <svg class="icon" viewBox="0 0 24 24" aria-hidden="true"><path d="M2 6.5V19h20V6.5l-10 7.5z M3 5h18l-9 6.8z"/></svg>
        vern@coastwardgoods.com.au
      </li>
      <li>
        <svg class="icon" viewBox="0 0 24 24" aria-hidden="true"><circle cx="12" cy="12" r="10"/><path d="M2 12h20M12 2c3 3 3 17 0 20M12 2c-3 3-3 17 0 20" fill="none" stroke="#262626" stroke-width="1.5"/></svg>
        <span>www.<strong>harbourlinesupply</strong>.com.au</span>
      </li>
    </ul>
    <p class="address">
      <svg class="icon" viewBox="0 0 20 26" aria-hidden="true"><path d="M10 0a10 10 0 0 0-10 10c0 7.5 10 16 10 16s10-8.5 10-16A10 10 0 0 0 10 0zm0 14a4 4 0 1 1 0-8 4 4 0 0 1 0 8z"/></svg>
      Adelaide, Brisbane and Darwin
    </p>
  </section>
</main>
</body>
</html>
```